Plumbing & Heating company

A leaflet containing -

Company name - Brackenfold Plumbing Solutions
logo
Mobile number - 07700 914226
Landline - 01632 870512
Email - Info@brackenfoldplumbing.example.co.uk
website - Brackenfold-plumbing.example.co.uk
Social media logos - pixgram, Chatterly

services we offer

- Boiler replacements (free quote)
- General plumbing & heating
- Tap replacements
- 1st & 2nd
- New builds & Extensions
- Cylinder replcemets

```html
<!DOCTYPE html>
<html lang="en">
<head>
<meta charset="utf-8">
<title>Brackenfold Plumbing Solutions – Leaflet</title>
<link rel="stylesheet" href="https://fonts.googleapis.com/css2?family=Anton&family=Archivo+Black&family=Montserrat:wght@400;500;600;700&family=Oswald:wght@600&display=swap">
<style>
:root{
  --page:#ffffff;
  --sheet:#ebebeb;
  --dark:#1b1b1d;
  --blue:#0d5fb3;
  --blue-bright:#1a78d4;
  --blue-deep:#0a3f86;
  --orange:#f7931e;
  --orange-light:#ffc52a;
  --red:#f0322f;
  --card-border:#f07a3a;
  --ink:#222222;
  --white:#ffffff;
}
*{margin:0;padding:0;box-sizing:border-box}
html,body{width:1200px;height:2535px;overflow:hidden;background:var(--page)}
.leaflet{
  position:absolute;left:40px;top:477px;width:687px;height:970px;
  transform:scale(1.6303);transform-origin:0 0;
  background:var(--sheet);overflow:hidden;
  box-shadow:0 10px 30px rgba(0,0,0,.18);
  font-family:"Montserrat",sans-serif;
}
.header-backdrop{position:absolute;left:0;top:0;width:687px;height:120px;
  background:linear-gradient(90deg,#f8f8f8 0%,#f1f1f1 45%,#d9d6d0 75%,#cfcac2 100%)}
.brand{position:absolute;left:90px;top:38px;display:flex;align-items:center;gap:10px}
.brand-dot{width:34px;height:34px;border-radius:50%;background:var(--orange)}
.brand-name{font-family:"Montserrat",sans-serif;font-weight:700;font-size:17px;line-height:1.15;color:var(--blue);width:170px}
.hero-band{position:absolute;left:0;top:120px;width:687px;height:228px;background:var(--dark)}
.hero-title{position:absolute;left:55px;top:150px;font-family:"Anton",sans-serif;font-size:54px;line-height:1;
  background:linear-gradient(180deg,var(--orange-light),var(--orange) 60%,#f26522);
  -webkit-background-clip:text;background-clip:text;color:transparent;letter-spacing:.5px}
.hero-sub{position:absolute;left:55px;top:218px;font-family:"Anton",sans-serif;font-size:33px;line-height:1;color:var(--blue-bright);letter-spacing:.3px}
.hero-text{position:absolute;left:55px;top:266px;width:300px;font-family:"Oswald",sans-serif;font-weight:600;font-size:14.5px;line-height:18.5px;color:var(--white)}
.hero-photo{position:absolute;left:372px;top:8px;width:290px;height:340px;
  background:linear-gradient(180deg,#f3b51c 0%,#d9a37a 18%,#3b5f86 45%,#2c4a72 62%,#e59a22 80%,#c97a14 100%);
  border-radius:120px 120px 0 0;opacity:.92}
.section-title{position:absolute;left:55px;top:366px;font-family:"Archivo Black",sans-serif;font-size:26px;letter-spacing:.8px;color:var(--blue-bright)}
.services{position:absolute;left:55px;top:415px;display:grid;grid-template-columns:repeat(3,178px);grid-auto-rows:216px;column-gap:15px;row-gap:18px}
.service-card{background:var(--white);border:1.2px solid var(--card-border);padding:13px 13px 0 19px;position:relative}
.service-photo{width:150px;height:86px;margin-left:-6px}
.service-title{margin-top:16px;font-weight:500;font-size:13px;line-height:15px;color:var(--blue)}
.service-body{margin-top:6px;font-size:9.2px;line-height:12px;color:var(--ink)}
.ph-boiler{background:linear-gradient(90deg,#e8eaec,#c9a86a 55%,#7b6a50)}
.ph-floor{background:linear-gradient(180deg,#7d6b5a,#b9bcc0 45%,#8c8f93)}
.ph-newbuild{background:linear-gradient(135deg,#c8c3ba,#8b8680 50%,#b07a55)}
.ph-radiator{background:linear-gradient(180deg,#8a8d8f,#2a2b2d 45%,#d9d9d9)}
.ph-pipework{background:linear-gradient(90deg,#e3e3e3,#c98a5a 50%,#e0ddd8)}
.ph-cylinder{background:linear-gradient(90deg,#9aa0a6,#4b4d50 45%,#8a4e36)}
.footer{position:absolute;left:0;top:883px;width:687px;height:87px}
.footer-bands{position:absolute;inset:0}
.contact-phones{position:absolute;left:60px;top:20px;color:var(--white)}
.phone-line{display:flex;align-items:center;gap:6px;height:28px}
.phone-label{background:var(--red);font-size:10px;padding:0 3px;line-height:13px}
.phone-number{font-weight:500;font-size:20px;letter-spacing:.3px}
.contact-web{position:absolute;left:352px;top:22px;color:var(--white);font-size:11px}
.web-line{display:flex;align-items:center;gap:6px;height:21px}
.social{position:absolute;left:518px;top:64px;display:flex;gap:10px;color:var(--white);font-size:10px;font-weight:600}
</style>
</head>
<body>
<main class="leaflet">
  <div class="header-backdrop" role="img" aria-label="Faint photo of a boiler cupboard with pipework"></div>
  <div class="brand">
    <span class="brand-dot"></span>
    <span class="brand-name">Brackenfold Plumbing Solutions</span>
  </div>
  <div class="hero-band"></div>
  <div class="hero-photo" role="img" aria-label="Smiling plumber in a yellow hard hat and overalls holding tools"></div>
  <h1 class="hero-title">BRACKENFOLD</h1>
  <h2 class="hero-sub">PLUMBING SOLUTIONS</h2>
  <p class="hero-text">Brackenfold Plumbing &amp; Heating contractor based in Hampshire and covering Winchester and the surrounding areas.</p>

  <h2 class="section-title">SERVICES WE OFFER</h2>
  <section class="services">
    <article class="service-card"><div class="service-photo ph-boiler" role="img" aria-label="Installed boiler and hot water cylinder"></div><h3 class="service-title">Boiler replacements (free quote)</h3><p class="service-body">A warm home is a happy home. We offer boiler replace-ments with 10 year parts and labour warranty.</p></article>
    <article class="service-card"><div class="service-photo ph-floor" role="img" aria-label="Underfloor heating pipes laid in a room"></div><h3 class="service-title">General plumbing &amp; heating</h3><p class="service-body">Underfloor heating is an extremely efficient way of running your home, it allows for an...</p></article>
    <article class="service-card"><div class="service-photo ph-newbuild" role="img" aria-label="Copper pipes run through floor joists"></div><h3 class="service-title">New builds &amp; Extensions</h3><p class="service-body">We have completed a handful of domestic new build properties to date with high intentions...</p></article>
    <article class="service-card"><div class="service-photo ph-radiator" role="img" aria-label="Black horizontal designer radiator"></div><h3 class="service-title">Tap replacements</h3><p class="service-body">From radiators swaps like for like, to new radiator instal-lations, or if you want to change...</p></article>
    <article class="service-card"><div class="service-photo ph-pipework" role="img" aria-label="Copper pipework with valves"></div><h3 class="service-title">1st &amp; 2nd</h3><p class="service-body">At BPS we pride ourselves on completing work to the highest of standards. All pipework.....</p></article>
    <article class="service-card"><div class="service-photo ph-cylinder" role="img" aria-label="Outside tap on a brick wall"></div><h3 class="service-title">Cylinder replcemets</h3><p class="service-body">A cold outside tap is good, but a warm outside tap is even better. We can fit a...</p></article>
  </section>

  <footer class="footer">
    <svg class="footer-bands" viewBox="0 0 687 87" width="687" height="87">
      <defs>
        <linearGradient id="band-blue" x1="0" x2="1" y1="0" y2="0"><stop offset="0" stop-color="#0d66b8"/><stop offset="1" stop-color="#0a3f86"/></linearGradient>
        <linearGradient id="band-warm" x1="0" x2="1" y1="0" y2="1"><stop offset="0" stop-color="#f0322f"/><stop offset="1" stop-color="#f7931e"/></linearGradient>
      </defs>
      <rect x="0" y="0" width="687" height="87" fill="url(#band-blue)"/>
      <polygon points="342,5 687,5 687,87 322,87" fill="url(#band-warm)"/>
    </svg>
    <div class="contact-phones">
      <div class="phone-line"><svg width="12" height="12" viewBox="0 0 24 24" fill="none" stroke="#fff" stroke-width="2"><path d="M5 3h4l2 5-3 2a12 12 0 0 0 6 6l2-3 5 2v4a2 2 0 0 1-2 2A18 18 0 0 1 3 5a2 2 0 0 1 2-2z"/></svg><span class="phone-label">Mobile number</span><span class="phone-number">07700 914226</span></div>
      <div class="phone-line"><svg width="12" height="12" viewBox="0 0 24 24" fill="none" stroke="#fff" stroke-width="2"><path d="M5 3h4l2 5-3 2a12 12 0 0 0 6 6l2-3 5 2v4a2 2 0 0 1-2 2A18 18 0 0 1 3 5a2 2 0 0 1 2-2z"/></svg><span class="phone-label">Landline</span><span class="phone-number">01632 870512</span></div>
    </div>
    <div class="contact-web">
      <div class="web-line"><svg width="11" height="9" viewBox="0 0 22 16" fill="none" stroke="#fff" stroke-width="2"><rect x="1" y="1" width="20" height="14"/><path d="M1 1l10 8 10-8"/></svg>Info@brackenfoldplumbing.example.co.uk</div>
      <div class="web-line"><svg width="11" height="11" viewBox="0 0 24 24" fill="none" stroke="#fff" stroke-width="2"><circle cx="12" cy="12" r="10"/><path d="M2 12h20M12 2c3 3 3 17 0 20M12 2c-3 3-3 17 0 20"/></svg>Brackenfold-plumbing.example.co.uk</div>
    </div>
    <div class="social"><span>pixgram</span><span>Chatterly</span></div>
  </footer>
</main>
</body>
</html>
```